Package Design for New Fruit Juice product - PEEL HAVEN

Our Company a Food and Beverage provider is launching 6 fruit juice variants.
We want to create the packaging for the different products.
The product name is Peel Haven (Logo attached) and this product is expected to be in the top category within the industry.
The startup products are
1) ORANGE JUICE
2) APPLE JUICE
3) MIXED BERRIES : apple, aronia, blackcurrant, strawberry
4) WHITE & RED GRAPE
5) CONCORD GRAPE
6) TROPICAL
There are 3 elements which we want to be incorporated into the front design.
1) a pouring effect : ie juice pouring from a source (if realistic, we want this source to be the spout of the box or you can create your own ideas)
2) a splash effect: the juice pours into a splash at the front of the box
3) the fruit(s) at the base of the box
a similar example is Volmi Juice: image attached to brief
We expect all product packages to follow similar design concept for consistency.
The colours to be used should match the respective fruits. Soft colors only, nothing too bold.
The Packaging type is the rectangular Cartovel (see attachments)
We invite creative and innovative designers to submit their designs for our project..
The deliverable is
1. Design in Keyline Design Sheet flat format
2. Design in Box format
3. For all 6 products
Kindly contact with any further information you may require in order to further understand this brief.
Finally, selected designer must commit to a 30day post project support, as design will be submitted for regulatory approval and very minor changes may be required.

```html
<!DOCTYPE html>
<html lang="en">
<head>
<meta charset="utf-8">
<title>Peel Haven – Juice Cartons</title>
<link href="https://fonts.googleapis.com/css2?family=Luckiest+Guy&family=Fredoka:wght@600&family=Open+Sans:wght@400;700&display=swap" rel="stylesheet">
<style>
  :root{
    --bg:#eceeee;
    --panel:#fbfbfa;
    --apple-side:#7b1f2c;
    --apple-title:#c8102e;
    --orange-side:#e29a1e;
    --orange-title:#ffffff;
    --ink:#1c1c1c;
    --pill:#5f9a2e;
    --brand:#2a2a2a;
    --brand-dot:#7ab23c;
  }
  *{box-sizing:border-box;margin:0;padding:0}
  html,body{width:1200px;height:1000px;overflow:hidden;background:var(--bg)}
  body{position:relative;font-family:"Open Sans",Arial,sans-serif;color:var(--ink)}

  .carton{position:absolute;top:150px;height:700px;display:flex;box-shadow:0 10px 30px rgba(0,0,0,.12)}
  .carton--apple{left:70px}
  .carton--orange{left:630px}

  .front{position:relative;width:300px;height:100%;background:var(--panel)}
  .side{position:relative;width:150px;height:100%;padding:70px 12px 0;color:#fff;font-size:7.5px;line-height:1.35}
  .carton--apple .side{background:var(--apple-side)}
  .carton--orange .side{background:var(--orange-side)}
  .top-band{position:absolute;left:0;right:0;top:0;height:22px}
  .carton--apple .top-band{background:var(--apple-side)}
  .carton--orange .top-band{background:var(--orange-side)}

  .fruit{position:absolute;left:42px;top:38px;width:216px;height:230px;border-radius:50%}
  .carton--apple .fruit{background:radial-gradient(circle at 50% 45%,#f6ecd6 0 52%,#e3cfa4 60%,#b51f2a 72%,#8e1420 100%)}
  .carton--orange .fruit{left:30px;top:30px;width:240px;height:240px;background:radial-gradient(circle,#fcc23a 0 30%,#f6a815 60%,#f9d67a 88%,#f49a10 100%)}

  .pour{position:absolute;left:118px;top:250px;width:64px;height:190px;border-radius:0 0 30px 30px}
  .carton--apple .pour{background:linear-gradient(180deg,rgba(214,170,110,.85),rgba(232,205,160,.5))}
  .carton--orange .pour{background:linear-gradient(180deg,rgba(248,200,70,.9),rgba(250,220,130,.5))}

  .splash{position:absolute;left:0;right:0;bottom:60px;height:230px}
  .carton--apple .splash{background:radial-gradient(ellipse at 60% 75%,rgba(190,130,70,.6),rgba(230,200,160,.25) 55%,transparent 75%)}
  .carton--orange .splash{background:radial-gradient(ellipse at 60% 75%,rgba(240,160,40,.6),rgba(250,215,140,.25) 55%,transparent 75%)}

  .product-title{position:absolute;left:0;right:0;top:90px;text-align:center;font-family:"Luckiest Guy",cursive;font-size:44px;line-height:1;letter-spacing:1px;-webkit-text-stroke:2px #222}
  .carton--apple .product-title{color:var(--apple-title)}
  .carton--orange .product-title{color:var(--orange-title);top:96px}

  .pill{position:absolute;left:50%;transform:translateX(-50%);top:196px;background:var(--pill);color:#fff;border:2px solid #fff;outline:1px solid #3d6b1a;border-radius:6px;padding:2px 10px;font-family:"Fredoka",sans-serif;font-size:11px;white-space:nowrap}

  .brand{position:absolute;left:0;right:0;top:452px;display:flex;align-items:center;justify-content:center;gap:8px}
  .brand-dot{width:16px;height:16px;border-radius:50%;background:var(--brand-dot)}
  .brand-name{font-family:"Fredoka",sans-serif;font-size:40px;line-height:1;color:var(--brand);text-align:center;width:150px}

  .base{position:absolute;left:8px;right:8px;bottom:10px;display:flex;align-items:flex-end;gap:8px}
  .volume{font-family:"Fredoka",sans-serif;font-size:22px;line-height:1}
  .volume small{font-size:12px}
  .gda{border-collapse:collapse;font-size:6px;text-align:center}
  .gda td{border:1px solid #333;padding:1px 3px;background:#fff}
  .gda tr.pct td{background:#222;color:#fff;font-weight:700;font-size:9px}
  .netwt{font-size:7px;font-weight:700;margin-left:auto}

  .side h4{font-size:7.5px;font-weight:700}
  .side p{margin-bottom:8px}
  .nutri{width:100%;border-collapse:collapse;font-size:5.5px;text-align:center;margin:6px 0 10px}
  .nutri td{border:1px solid rgba(255,255,255,.6);height:26px}
</style>
</head>
<body>

<section class="carton carton--apple" aria-label="Apple juice carton">
  <div class="front">
    <div class="top-band"></div>
    <div class="fruit" role="img" aria-label="Photo of a halved red apple"></div>
    <div class="pour" role="img" aria-label="Apple juice pouring from the fruit"></div>
    <div class="splash" role="img" aria-label="Apple juice splash"></div>
    <h1 class="product-title">APPLE<br>JUICE</h1>
    <span class="pill">Premium Fruit Juice</span>
    <div class="brand"><span class="brand-dot"></span><span class="brand-name">Peel Haven</span></div>
    <div class="base">
      <span class="volume">e1<small>L</small></span>
      <table class="gda">
        <tr><td>Calories<br>33 kcal</td><td>Sugar<br>7.7g</td><td>Fat<br>0.0g</td><td>Saturates<br>0.0g</td><td>Salt<br>0.0g</td></tr>
        <tr class="pct"><td>2%</td><td>9%</td><td>0%</td><td>0%</td><td>0%</td></tr>
      </table>
      <span class="netwt">Net Wt. 30 fl.oz</span>
    </div>
  </div>
  <div class="side">
    <h4>Ingredients [en]</h4>
    <p>Purified water, Orange Juice, Apple Juice, Ruby Grapefruit, Lemon Juice</p>
    <h4>Ingredients [fr]</h4>
    <p>Eau purifiée, jus d'orange, jus de pomme, de pamplemousse Ruby, jus de citron</p>
    <p>NUTRITIONAL INFORMATION TABLE, USE 250ML SERVING</p>
    <table class="nutri">
      <tr><td>energy</td><td>concentrate</td><td>energy</td><td>energy</td></tr>
      <tr><td>energy</td><td>1145</td><td>0</td><td>65</td></tr>
      <tr><td>energy</td><td>0</td><td>1145</td><td>1145</td></tr>
      <tr><td>energy</td><td>65</td><td>65</td><td>1145</td></tr>
      <tr><td>energy</td><td>0</td><td>0</td><td>65</td></tr>
      <tr><td>energy</td><td>0</td><td>1145</td><td>0</td></tr>
      <tr><td>energy</td><td>0</td><td>1145</td><td>0</td></tr>
      <tr><td>energy</td><td>0</td><td>1145</td><td>1145</td></tr>
      <tr><td>energy</td><td>0</td><td>1145</td><td>65</td></tr>
    </table>
    <p>**NOTE TO DESIGNERS: use 250ml serving information only in design</p>
    <p>The trademark Peel Haven™, Peel Haven logo, and green explosion design are the properties of Marlowe Food Company Limited.</p>
  </div>
</section>

<section class="carton carton--orange" aria-label="Orange juice carton">
  <div class="front">
    <div class="top-band"></div>
    <div class="fruit" role="img" aria-label="Photo of an orange slice"></div>
    <div class="pour" role="img" aria-label="Orange juice pouring from the fruit"></div>
    <div class="splash" role="img" aria-label="Orange juice splash"></div>
    <h1 class="product-title">ORANGE<br>JUICE</h1>
    <span class="pill">Premium Fruit Juice</span>
    <div class="brand"><span class="brand-dot"></span><span class="brand-name">Peel Haven</span></div>
    <div class="base">
      <span class="volume">e1<small>L</small></span>
      <table class="gda">
        <tr><td>Calories<br>33 kcal</td><td>Sugar<br>7.7g</td><td>Fat<br>0.0g</td><td>Saturates<br>0.0g</td><td>Salt<br>0.0g</td></tr>
        <tr class="pct"><td>2%</td><td>9%</td><td>0%</td><td>0%</td><td>0%</td></tr>
      </table>
      <span class="netwt">Net Wt. 30 fl.oz</span>
    </div>
  </div>
  <div class="side">
    <h4>Ingredients [en]</h4>
    <p>Purified water, Orange Juice, Apple Juice, Ruby Grapefruit, Lemon Juice</p>
    <h4>Ingredients [fr]</h4>
    <p>Eau purifiée, jus d'orange, jus de pomme, de pamplemousse Ruby, jus de citron</p>
    <p>NUTRITIONAL INFORMATION TABLE, USE 250ML SERVING</p>
    <table class="nutri">
      <tr><td>energy</td><td>concentrate</td><td>energy</td><td>energy</td></tr>
      <tr><td>energy</td><td>1145</td><td>0</td><td>65</td></tr>
      <tr><td>energy</td><td>0</td><td>1145</td><td>1145</td></tr>
      <tr><td>energy</td><td>65</td><td>65</td><td>1145</td></tr>
      <tr><td>energy</td><td>0</td><td>0</td><td>65</td></tr>
      <tr><td>energy</td><td>0</td><td>1145</td><td>0</td></tr>
      <tr><td>energy</td><td>0</td><td>1145</td><td>0</td></tr>
      <tr><td>energy</td><td>0</td><td>1145</td><td>1145</td></tr>
      <tr><td>energy</td><td>0</td><td>1145</td><td>65</td></tr>
    </table>
    <p>**NOTE TO DESIGNERS: use 250ml serving information only in design</p>
    <p>The trademark Peel Haven™, Peel Haven logo, and green explosion design are the properties of Marlowe Food Company Limited.</p>
  </div>
</section>

</body>
</html>
```